Halden Herd Services concrete grooving services flyer design

Halden Herd Services offers 4 different grooving options:

DEEP GROOVING
, ideal for Safety & Efficiency
Our hugely popular deep straight line grooving, long lasting, minimal hoof wear,

Create safe and secure flooring, cows walk without hesitation

Achieve groove spacing for optimal hoof function, reduce hoof trauma

Ideal grooves to new concrete or surfaces with little to no pattern or previous grooving

Ideal groove pattern as promoted by The pasturefield project

MINI GROOVING,
Smaller dimensions Ideal option for heifer housing and high activity areas such as parlours and handling areas

An ideal solution for regaining traction on old previous grooving that has lost its traction without loosing stability

Plaining

smoothing down rough concrete with previous aggressive grooving or patterns to reduce hoof trauma & wear

SENSOR PLATE SINKING

sinking sensor plates for automated machines below surface level preventing accidental damage & wear

```html
<!DOCTYPE html>
<html lang="en">
<head>
<meta charset="utf-8">
<title>Halden Herd Services – Concrete Grooving Services</title>
<link href="https://fonts.googleapis.com/css2?family=Open+Sans:wght@400;600;700&family=Montserrat:wght@500;700;800&display=swap" rel="stylesheet">
<style>
  :root {
    --green: #8cc63f;
    --green-dark: #1f7a3a;
    --ink: #1f2223;
    --ink-soft: #3a3d3f;
    --bg-top: #e9ecea;
    --bg-bottom: #dfe3e1;
    --white: #ffffff;
  }
  * { box-sizing: border-box; margin: 0; padding: 0; }
  html, body { width: 1200px; height: 1200px; overflow: hidden; }
  body { font-family: "Open Sans", Arial, sans-serif; color: var(--ink); background: var(--white); }

  .flyer { position: relative; width: 1200px; height: 1200px; overflow: hidden; }

  .barn-backdrop {
    position: absolute; inset: 0;
    background: linear-gradient(180deg, var(--bg-top) 0%, #eef0ee 45%, var(--bg-bottom) 100%);
  }

  .hero-photo { position: absolute; top: 0; right: 0; width: 560px; height: 560px; }

  .brand {
    position: absolute; left: 90px; top: 28px; width: 230px;
    display: flex; flex-direction: column; align-items: center;
    color: var(--ink);
  }
  .brand-dot { width: 96px; height: 96px; border-radius: 50%; background: var(--ink); margin-bottom: 14px; }
  .brand-name {
    font-family: "Open Sans", Arial, sans-serif; font-weight: 700;
    font-size: 27px; line-height: 1.1; text-align: center; letter-spacing: 1px;
    text-transform: uppercase;
  }

  .tagline-band {
    position: absolute; left: 0; top: 228px; width: 760px; height: 88px;
    background: var(--green);
  }
  .tagline-tab {
    position: absolute; left: 38px; top: 250px; width: 66px; height: 46px;
    background: var(--green-dark); border-radius: 4px 24px 24px 4px;
  }
  .tagline {
    position: absolute; left: 120px; top: 244px;
    font-family: "Montserrat", Arial, sans-serif; font-weight: 500;
    font-size: 21px; line-height: 29px; letter-spacing: 4px;
    color: var(--ink); text-transform: uppercase;
  }

  .section-title {
    position: absolute; left: 72px; top: 338px;
    font-family: "Montserrat", Arial, sans-serif; font-weight: 800;
    font-size: 30px; letter-spacing: 5px; color: var(--ink);
  }
  .section-title em { font-style: normal; color: var(--green-dark); }

  .service { position: absolute; left: 72px; display: flex; }
  .service-thumb {
    width: 142px; height: 140px; flex: none;
    border: 6px solid var(--green); border-radius: 18px;
  }
  .service-body { margin-left: 14px; }
  .service-heading {
    font-family: "Open Sans", Arial, sans-serif; font-weight: 700;
    font-size: 20px; color: var(--ink); margin-top: -2px;
  }
  .service-heading span { border-bottom: 2px solid var(--ink-soft); padding-bottom: 1px; }
  .service-note { font-size: 13px; letter-spacing: 0.6px; margin: 4px 0 2px 16px; color: var(--ink-soft); }
  .service-points { list-style: none; margin-left: 16px; margin-top: 8px; }
  .service-points li {
    position: relative; padding-left: 14px;
    font-size: 18px; line-height: 24px; color: var(--ink);
  }
  .service-points li.arrow::before {
    content: ""; position: absolute; left: 0; top: 8px;
    border-left: 7px solid var(--green); border-top: 4px solid transparent; border-bottom: 4px solid transparent;
  }
  .service-points li + li.arrow { margin-top: 2px; }

  .contact-bar {
    position: absolute; left: 0; top: 1092px; width: 1200px; height: 84px;
    background: var(--green); display: flex; align-items: center;
    color: var(--white); font-size: 30px;
  }
  .contact-item { display: flex; align-items: center; }
  .contact-email { margin-left: 114px; }
  .contact-social { margin-left: 58px; }
  .icon-ring {
    width: 46px; height: 46px; border-radius: 50%; border: 3px solid var(--white);
    display: flex; align-items: center; justify-content: center; margin-right: 12px;
  }
  .footer-strip { position: absolute; left: 0; top: 1176px; width: 1200px; height: 24px; background: #f2f3f2; }
</style>
</head>
<body>
<main class="flyer">
  <div class="barn-backdrop" role="img" aria-label="Faded interior of a cattle barn with grooved concrete floor"></div>

  <svg class="hero-photo" viewBox="0 0 560 560" role="img" aria-label="Grooving machine working on a wet barn concrete floor">
    <defs>
      <linearGradient id="heroTone" x1="0" y1="0" x2="1" y2="1">
        <stop offset="0" stop-color="#6d7570"/>
        <stop offset="0.5" stop-color="#a89a78"/>
        <stop offset="1" stop-color="#8a6a3a"/>
      </linearGradient>
    </defs>
    <path d="M8,0 H560 V548 L540,546 L50,62 Q10,22 8,0 Z" fill="url(#heroTone)" stroke="#8cc63f" stroke-width="9"/>
  </svg>

  <div class="brand">
    <div class="brand-dot"></div>
    <div class="brand-name">Halden Herd<br>Services</div>
  </div>

  <div class="tagline-band"></div>
  <div class="tagline-tab"></div>
  <p class="tagline">Concrete grooving services<br>from a hoof health perspective</p>

  <h2 class="section-title">SERVICES <em>OFFERED</em></h2>

  <section class="service" style="top:398px">
    <div class="service-thumb" role="img" aria-label="Deep straight-line grooves in barn concrete" style="background:linear-gradient(135deg,#7a6a3c,#b39a52)"></div>
    <div class="service-body">
      <h3 class="service-heading">1. <span>DEEP GROOVING</span></h3>
      <p class="service-note">ideal for Safety &amp; Efficiency</p>
      <ul class="service-points" style="margin-top:0">
        <li class="arrow">Our hugely popular deep straight line grooving, long lasting,<br>minimal hoof wear.</li>
        <li class="arrow">Create safe and secure flooring, cows walk without hesitation</li>
        <li class="arrow">Achieve groove spacing for optimal hoof function, reduce hoof trauma</li>
        <li>Ideal grooves to new concrete or surfaces with little to no pattern or previous grooving</li>
        <li>Ideal groove pattern as promoted by The pasturefield project</li>
      </ul>
    </div>
  </section>

  <section class="service" style="top:607px">
    <div class="service-thumb" role="img" aria-label="Short mini grooves cut into concrete" style="background:linear-gradient(135deg,#5e5650,#9a8e82)"></div>
    <div class="service-body">
      <h3 class="service-heading">2. <span>MINI GROOVING</span></h3>
      <ul class="service-points">
        <li class="arrow">Smaller dimensions Ideal option for heifer housing and high activity areas<br>such as parlours and handling areas</li>
        <li class="arrow">An ideal solution for regaining traction on old previous grooving<br>that has lost its traction without loosing stability</li>
      </ul>
    </div>
  </section>

  <section class="service" style="top:771px">
    <div class="service-thumb" role="img" aria-label="Scraper track channel cut into concrete" style="background:linear-gradient(180deg,#8a7f74,#4d4a47)"></div>
    <div class="service-body">
      <h3 class="service-heading">3. <span>SCRAPER TRACKS / SENSOR PLATE SINKING</span></h3>
      <ul class="service-points">
        <li class="arrow">Larger spaced cuts available to sink sensor plates for robots or</li>
        <li class="arrow">Automatic Scraper track Lines</li>
      </ul>
    </div>
  </section>

  <section class="service" style="top:933px">
    <div class="service-thumb" role="img" aria-label="Planed smooth concrete surface" style="background:linear-gradient(135deg,#6f7b82,#a7adb0)"></div>
    <div class="service-body">
      <h3 class="service-heading">4. <span>PLAINING</span></h3>
      <ul class="service-points">
        <li class="arrow">Smoothing down rough concrete with previous aggressive grooving or patterns<br>to reduce hoof trauma &amp; wear</li>
      </ul>
    </div>
  </section>

  <footer class="contact-bar">
    <div class="contact-item contact-email">
      <span class="icon-ring">
        <svg width="24" height="20" viewBox="0 0 24 20" aria-hidden="true">
          <rect x="1.5" y="2" width="21" height="16" rx="2" fill="none" stroke="#fff" stroke-width="2.5"/>
          <path d="M2 3 L12 11 L22 3" fill="none" stroke="#fff" stroke-width="2.5"/>
        </svg>
      </span>
      haldenherdservices@mailbox.com
    </div>
    <div class="contact-item contact-social">
      <span class="icon-ring"></span>
      <span class="icon-ring"></span>
      Halden herd services
    </div>
  </footer>
  <div class="footer-strip"></div>
</main>
</body>
</html>
```